Simple proffessional BC

I have a logo which I will attach below.
I would like the logo on the front of the card with these details in point form below:
Pre and Post Natal Yoga: Pregnancy Workshops: Hypnobirthing Courses
On the back of the card my details:
Merrin Galvey
Facebook page- calmbellieswillowharbour
Mobile- 0438 512 740

I like the idea of the card being simple, possibly just the above on a plain coloured (eggshell?) card, a card that is textured.
I am open to suggestion if it appeals!
Thank you and good luck!

Target Market(s)

Pregnant women, 20's-40's

Requirements
Must have
• Simple, compliment logo.
Make logo the feature.
Should not have

• .

```html
<!DOCTYPE html>
<html lang="en">
<head>
<meta charset="utf-8">
<title>Calm Bellies – Business Card</title>
<link rel="stylesheet" href="https://fonts.googleapis.com/css2?family=Baloo+2:wght@700&family=Josefin+Sans:wght@300;400&family=Arimo&display=swap">
<style>
  :root {
    --page: #e9e7e5;
    --card-white: #fbfaf8;
    --mauve: #b7abab;
    --cream: #f1e7d8;
    --wine: #7c1517;
    --saffron: #e7a33b;
    --ink: #2a1c1c;
    --card-w: 880px;
    --card-h: 503px;
  }
  * { margin: 0; padding: 0; box-sizing: border-box; }
  html, body {
    width: 1037px; height: 1200px; overflow: hidden;
    background: var(--page);
  }
  .sheet { position: relative; width: 1037px; height: 1200px; }
  .card {
    position: absolute; left: 78px;
    width: var(--card-w); height: var(--card-h);
    background: var(--card-white);
    overflow: hidden;
    box-shadow: 0 6px 18px rgba(0,0,0,0.18);
  }
  .card--details { top: 60px; }
  .card--brand { top: 637px; }
  .card__shapes { position: absolute; inset: 0; }

  .holder-name {
    position: absolute; left: 40px; top: 40px;
    font-family: "Baloo 2", "Arial Black", sans-serif;
    font-weight: 700; font-size: 60px; line-height: 1;
    font-variant: small-caps; letter-spacing: 0.5px;
    color: var(--wine);
  }
  .contact-list {
    position: absolute; left: 40px; top: 352px;
    list-style: none;
    font-family: "Arimo", Arial, sans-serif;
    font-size: 19px; color: var(--saffron);
  }
  .contact-list__item {
    display: flex; align-items: center; gap: 16px;
    height: 30px; margin-bottom: 22px;
  }
  .contact-list__icon { width: 22px; height: 22px; flex: none; }

  .brand-lockup {
    position: absolute; left: 96px; top: 150px;
    display: flex; align-items: center; gap: 40px;
  }
  .brand-lockup__disc {
    width: 140px; height: 140px; border-radius: 50%;
    background: var(--saffron); flex: none;
  }
  .brand-lockup__name {
    font-family: "Josefin Sans", Arial, sans-serif;
    font-weight: 300; font-size: 80px; line-height: 1;
    color: var(--wine); white-space: nowrap;
  }
  .service-list {
    position: absolute; left: 96px; top: 352px; width: 640px;
    list-style: none;
    display: flex; flex-wrap: wrap; gap: 6px 0;
    font-family: "Josefin Sans", Arial, sans-serif;
    font-weight: 400; font-size: 21px; line-height: 1.3;
    color: var(--wine);
  }
  .service-list__item { white-space: nowrap; }
  .service-list__item + .service-list__item::before {
    content: "•"; color: var(--saffron); margin: 0 12px;
  }
</style>
</head>
<body>
<main class="sheet">

  <section class="card card--details" aria-label="Card back with contact details">
    <svg class="card__shapes" width="880" height="503" viewBox="0 0 880 503" aria-hidden="true">
      <defs>
        <clipPath id="band-clip">
          <rect x="0" y="0" width="632" height="503"/>
          <circle cx="632" cy="210" r="280"/>
        </clipPath>
      </defs>
      <rect class="side-panel" x="600" y="0" width="280" height="503" fill="var(--mauve)"/>
      <circle class="sun-circle" cx="632" cy="210" r="280" fill="var(--cream)"/>
      <rect class="wine-band" x="0" y="255" width="880" height="248" fill="var(--wine)" clip-path="url(#band-clip)"/>
      <circle cx="632" cy="210" r="280" fill="#ffffff" opacity="0.06"/>
      <line class="name-rule" x1="40" y1="127" x2="726" y2="127" stroke="var(--ink)" stroke-width="2.5"/>
    </svg>

    <h1 class="holder-name">Merrin Galvey</h1>

    <ul class="contact-list">
      <li class="contact-list__item">
        <svg class="contact-list__icon" viewBox="0 0 22 22" aria-hidden="true">
          <circle cx="11" cy="11" r="10" fill="#3b5998"/>
        </svg>
        <span>calmbellieswillowharbour</span>
      </li>
      <li class="contact-list__item">
        <svg class="contact-list__icon" viewBox="0 0 22 22" aria-hidden="true">
          <rect x="6" y="2" width="10" height="18" rx="1.5" fill="none" stroke="#f4f0ea" stroke-width="1.6"/>
          <line x1="9.5" y1="17" x2="12.5" y2="17" stroke="#f4f0ea" stroke-width="1.4"/>
        </svg>
        <span>0438 512 740</span>
      </li>
    </ul>
  </section>

  <section class="card card--brand" aria-label="Card front with brand name and services">
    <svg class="card__shapes" width="880" height="503" viewBox="0 0 880 503" aria-hidden="true">
      <rect class="side-panel" x="0" y="0" width="880" height="503" fill="var(--mauve)"/>
      <path class="saffron-rim" d="M-2 -2 H600 A258 258 0 0 1 600 514 H-2 Z" transform="translate(14 6)" fill="var(--saffron)"/>
      <path class="white-field" d="M-2 -2 H600 A258 258 0 0 1 600 514 H-2 Z" fill="var(--card-white)" stroke="var(--wine)" stroke-width="1.5"/>
    </svg>

    <div class="brand-lockup">
      <span class="brand-lockup__disc" aria-hidden="true"></span>
      <span class="brand-lockup__name">Calm Bellies</span>
    </div>

    <ul class="service-list" aria-label="Services">
      <li class="service-list__item">Pre and Post Natal Yoga</li>
      <li class="service-list__item">Pregnancy Workshops</li>
      <li class="service-list__item">Hypnobirthing Courses</li>
    </ul>
  </section>

</main>
</body>
</html>
```